Business Card Design Project

business cards to match the logo design reference 1970674
specific details to be provided asap - message to follow
hello - thank you for the logo design (reference 1970674) which we are very happy with. In terms of business cards you presented a couple of options ie blue front/white back and then the reverse. Can we start with the white front version but change the text details to black font?
Actual details are as follows;
Dorian Plimsoll
Managing Director
e dorianplimsoll@kestrowe.com.au
t +61 2 5550 1937
m +61 400 555 219
Suite 712, Level 7, 48 Thornbury Rd
Sydney, NSW 2000, Australia
www.kestrowe.com.au

```html
<!DOCTYPE html>
<html lang="en">
<head>
<meta charset="utf-8">
<title>Kestrowe Business Cards</title>
<link href="https://fonts.googleapis.com/css2?family=Open+Sans:wght@400;600&display=swap" rel="stylesheet">
<style>
  :root {
    --bg: #e9e6e0;
    --card-white: #ffffff;
    --sky: #3fb0e0;
    --sky-light: #7fcbef;
    --navy-top: #3a6fa5;
    --navy-bottom: #163e74;
    --ink: #1b1b1b;
    --logo-grey: #6f7378;
    --rule: #9a9ea3;
  }
  * { margin: 0; padding: 0; box-sizing: border-box; }
  html, body { width: 1200px; height: 675px; overflow: hidden; }
  body {
    background: var(--bg);
    font-family: "Open Sans", Arial, sans-serif;
    position: relative;
  }
  .card {
    position: absolute;
    top: 184px;
    width: 510px;
    height: 307px;
    border-radius: 3px;
    overflow: hidden;
    box-shadow: 0 6px 18px rgba(0,0,0,0.18);
  }
  /* Front */
  .card-front { left: 60px; background: var(--card-white); }
  .front-brand {
    position: absolute;
    left: 30px; top: 104px;
    display: flex; align-items: center; gap: 10px;
  }
  .brand-dot {
    width: 22px; height: 22px; border-radius: 50%;
    background: var(--sky);
  }
  .brand-name {
    font-size: 34px; font-weight: 600; color: var(--logo-grey);
    letter-spacing: 0.5px;
  }
  .divider {
    position: absolute; left: 232px; top: 74px;
    width: 1px; height: 108px; background: var(--rule);
  }
  .contact {
    position: absolute; left: 256px; top: 40px; right: 20px;
    color: var(--ink); font-size: 10.5px; line-height: 1.45;
  }
  .person-name { color: var(--sky); font-size: 15px; font-weight: 400; line-height: 1.2; }
  .person-title { font-size: 11px; margin-bottom: 16px; }
  .address { margin-bottom: 14px; }
  .line { display: flex; align-items: center; gap: 6px; }
  .line svg { width: 10px; height: 10px; flex: none; }
  .band {
    position: absolute; left: 0; right: 0; bottom: 0; height: 38px;
    background: var(--sky);
  }
  .band-url {
    position: absolute; left: 150px; bottom: 11px;
    color: #fff; font-size: 13px; letter-spacing: 3px;
  }
  .tile { position: absolute; background: var(--sky); }
  .tile-light { background: var(--sky-light); }
  /* Back */
  .card-back {
    left: 630px;
    background: linear-gradient(160deg, var(--navy-top), var(--navy-bottom));
  }
  .back-brand {
    position: absolute; left: 0; right: 0; top: 118px;
    display: flex; justify-content: center; align-items: center; gap: 12px;
  }
  .back-brand .brand-dot { background: #ffffff; width: 24px; height: 24px; }
  .back-brand .brand-name { color: #ffffff; font-size: 40px; }
  .back-url {
    position: absolute; left: 0; right: 0; bottom: 44px; text-align: center;
    color: #ffffff; font-size: 12px; letter-spacing: 3px;
  }
</style>
</head>
<body>
  <section class="card card-front">
    <div class="front-brand">
      <span class="brand-dot"></span>
      <span class="brand-name">Kestrowe</span>
    </div>
    <div class="divider"></div>
    <div class="contact">
      <p class="person-name">Dorian Plimsoll</p>
      <p class="person-title">Managing Director</p>
      <p class="address">Suite 712, Level 7, 48 Thornbury Rd<br>Sydney, NSW 2000, Australia</p>
      <p class="line">
        <svg viewBox="0 0 10 10"><path d="M2 1 L4 1 L4.6 3 L3.4 3.8 Q4.4 5.8 6.2 6.6 L7 5.4 L9 6 L9 8 Q5 9.5 2 5 Q1 3 2 1 Z" fill="var(--sky)"/></svg>
        +61 2 5550 1937
      </p>
      <p class="line">
        <svg viewBox="0 0 10 10"><rect x="2.5" y="0.5" width="5" height="9" rx="1" fill="var(--sky)"/><rect x="3.5" y="1.8" width="3" height="5.4" fill="#fff"/></svg>
        +61 400 555 219
      </p>
      <p class="line">
        <svg viewBox="0 0 10 10"><rect x="0.5" y="2" width="9" height="6.5" fill="none" stroke="var(--sky)" stroke-width="1"/><path d="M0.8 2.3 L5 5.6 L9.2 2.3" fill="none" stroke="var(--sky)" stroke-width="1"/></svg>
        dorianplimsoll@kestrowe.com.au
      </p>
    </div>
    <div class="band"><span class="band-url">www.kestrowe.com.au</span></div>
    <span class="tile" style="right:0; bottom:38px; width:44px; height:18px;"></span>
    <span class="tile tile-light" style="right:44px; bottom:38px; width:22px; height:10px;"></span>
    <span class="tile" style="right:0; bottom:62px; width:20px; height:14px;"></span>
    <span class="tile tile-light" style="right:26px; bottom:62px; width:14px; height:8px;"></span>
  </section>

  <section class="card card-back">
    <div class="back-brand">
      <span class="brand-dot"></span>
      <span class="brand-name">Kestrowe</span>
    </div>
    <p class="back-url">www.kestrowe.com.au</p>
  </section>
</body>
</html>
```